Trifold for Integrated Healthcare Business. 1 of 13 that we will need!

Hi! I would like to start off making a general trifold brochure for our practice that we can distribute to other healthcare offices. The intention of this trifold is to equip referral partners with something to distribute to their patients and clients that will give them information about our office and help them create a 'warm' handoff to our practice. We would also hand this out at marketing events. I can provide as much information as needed, but we have plenty of content on our website(s). I'd like this brochure to tie-in our chiropractic, physical therapy, and medical services.

Target Market(s)

People interested in chiropractic, physical therapy, or regenerative medical services

Industry/Entity Type

Healhcare

Font styles to use
Other font styles liked:
• Chalet (See Graphics Standards Attached)

Requirements
Must have
• Our contact information (www.marlowcarehealth.com)
Nice to have
• Clean, engaging, and professional. I'd like to make this look and feel like a high-level trusted healthcare organization
Should not have
• I don't want this to be too text heavy, but a good balance between images, text, contact info, and a call to action.

```html
<!DOCTYPE html>
<html lang="en">
<head>
<meta charset="utf-8">
<title>Marlowcare Trifold Brochure</title>
<link rel="stylesheet" href="https://fonts.googleapis.com/css2?family=Montserrat:wght@600;700;800&display=swap">
<style>
  :root{
    --stage:#7b7a7b;
    --ink:#3a3a3d;
    --dark:#38383b;
    --blue:#2aa5de;
    --white:#ffffff;
  }
  *{box-sizing:border-box;margin:0;padding:0}
  html,body{width:1200px;height:1200px;overflow:hidden;background:var(--stage)}
  body{font-family:"Montserrat",Arial,sans-serif;position:relative}
  .brochure{position:absolute;left:60px;top:182px;width:1080px;height:835px;overflow:hidden;box-shadow:0 18px 40px rgba(0,0,0,.35)}
  .brochure-art{position:absolute;inset:0;display:block}
  .cover-headline{position:absolute;left:34px;top:660px;width:310px;color:var(--ink);font-weight:800;font-size:36px;line-height:1.1;white-space:nowrap}
  .contact{position:absolute;left:360px;width:360px;color:var(--white);font-weight:700;text-align:center;white-space:nowrap}
  .address{top:478px;font-size:22px;line-height:1.3}
  .web{top:642px;font-size:18px;letter-spacing:.2px}
  .phone{top:754px;font-size:28px;letter-spacing:.5px}
  .brand{position:absolute;left:720px;top:150px;width:360px;display:flex;justify-content:center;align-items:center;gap:12px}
  .brand-dot{width:24px;height:24px;border-radius:50%;background:var(--blue);flex:none}
  .brand-name{font-weight:700;font-size:32px;color:var(--ink);letter-spacing:-.3px}
  .approach-headline{position:absolute;left:748px;top:690px;width:316px;color:var(--white);font-weight:800;font-size:31px;line-height:1.18;white-space:nowrap}
</style>
</head>
<body>
  <div class="brochure">
    <svg class="brochure-art" viewBox="0 0 1080 835" width="1080" height="835">
      <defs>
        <linearGradient id="lightFade" x1="0" y1="0" x2="0" y2="1">
          <stop offset="0" stop-color="#fafafa"/>
          <stop offset="1" stop-color="#d6d6d7"/>
        </linearGradient>
        <linearGradient id="blueFade" x1="0" y1="0" x2="0" y2="1">
          <stop offset="0" stop-color="#27a9e6"/>
          <stop offset="1" stop-color="#2196d0"/>
        </linearGradient>
        <linearGradient id="gymPhoto" x1="0" y1="0" x2="1" y2="1">
          <stop offset="0" stop-color="#e8e4df"/>
          <stop offset=".45" stop-color="#3e5a8c"/>
          <stop offset="1" stop-color="#4a3f3a"/>
        </linearGradient>
        <linearGradient id="treatPhoto" x1="0" y1="0" x2="1" y2="1">
          <stop offset="0" stop-color="#e6e4e2"/>
          <stop offset=".55" stop-color="#b7b2ae"/>
          <stop offset="1" stop-color="#252527"/>
        </linearGradient>
      </defs>

      <!-- left panel -->
      <rect x="0" y="0" width="360" height="835" fill="url(#lightFade)"/>
      <path fill="var(--dark)" d="M0 0H360V330C330 340 300 360 290 380C270 405 230 410 170 410C110 410 50 405 0 420Z"/>
      <path fill="var(--dark)" d="M280 370C320 380 345 430 330 480C360 520 350 600 295 618C240 636 200 595 210 550C220 510 255 500 250 470C245 440 245 380 280 370Z"/>

      <!-- middle panel -->
      <rect x="360" y="0" width="360" height="835" fill="url(#blueFade)"/>
      <g role="img" aria-label="Faint background photo of the clinic treatment room">
        <rect x="360" y="0" width="360" height="420" fill="#1d8fc8" opacity=".25"/>
      </g>
      <circle cx="395" cy="332" r="78" fill="var(--dark)"/>

      <!-- left photo circle -->
      <circle cx="190" cy="200" r="158" fill="var(--blue)"/>
      <g role="img" aria-label="Photo of a clinician guiding a patient through a shoulder exercise in the rehab gym">
        <circle cx="190" cy="200" r="150" fill="url(#gymPhoto)"/>
      </g>

      <!-- right panel -->
      <rect x="720" y="0" width="360" height="835" fill="url(#lightFade)"/>
      <g role="img" aria-label="Faint background photo of the clinic front desk">
        <rect x="720" y="0" width="360" height="420" fill="#ffffff" opacity=".35"/>
      </g>
      <path fill="var(--dark)" d="M720 470C760 460 790 520 900 600C1000 630 1060 560 1080 520V835H720Z"/>
      <circle cx="900" cy="440" r="170" fill="var(--white)"/>
      <circle cx="900" cy="440" r="162" fill="var(--blue)"/>
      <g role="img" aria-label="Photo of a practitioner treating a patient's forearm on a treatment table">
        <circle cx="900" cy="440" r="154" fill="url(#treatPhoto)"/>
      </g>

      <!-- fold lines -->
      <line x1="360" y1="0" x2="360" y2="835" stroke="#000" stroke-opacity=".08"/>
      <line x1="720" y1="0" x2="720" y2="835" stroke="#000" stroke-opacity=".08"/>

      <!-- icons -->
      <g class="icon-house" fill="none" stroke="#fff" stroke-width="3" stroke-linejoin="round">
        <path d="M516 448L540 428L564 448"/>
        <rect x="522" y="446" width="36" height="22"/>
        <rect x="534" y="454" width="10" height="14"/>
        <path d="M556 436V428H562V442"/>
      </g>
      <g class="icon-globe" fill="none" stroke="#fff" stroke-width="2.5">
        <circle cx="540" cy="607" r="20"/>
        <ellipse cx="540" cy="607" rx="9" ry="20"/>
        <line x1="520" y1="607" x2="560" y2="607"/>
        <path d="M523 597H557M523 617H557"/>
      </g>
      <g class="icon-phone">
        <rect x="520" y="702" width="40" height="38" rx="7" fill="#fff"/>
        <path d="M534 710C530 714 530 726 538 732L543 728L539 722L541 720L536 712Z" fill="var(--blue)"/>
      </g>
    </svg>

    <h2 class="cover-headline">Begin Your<br>Journey to<br>Better Health</h2>

    <p class="contact address">1580 Harbor Ave Ste. 300<br>Linden Park, TX 75123</p>
    <p class="contact web">www.marlowcarehealth.com</p>
    <p class="contact phone">(555) 014-2760</p>

    <div class="brand">
      <span class="brand-dot"></span>
      <span class="brand-name">marlowcare</span>
    </div>

    <h2 class="approach-headline">A New Approach<br>To Healthcare</h2>
  </div>
</body>
</html>
```